Afternoon Soiree Garden Party Invitation

Invitation design for an 'Afternoon Soirée' backyard garden party.
Format is for-print and mailing and can be either double-sided design to be enveloped and mailed or it can be a postcard-style with design on one side and address/postage placeholder on the reverse side.
Text, dimensions and additional information in the provided Word document.
Font styles to use
Script
Requirements
Must have
- Elegant, yet easy-going and warm/welcoming feel

```html
<!DOCTYPE html>
<html lang="en">
<head>
<meta charset="utf-8">
<title>Afternoon Soirée Invitation</title>
<link href="https://fonts.googleapis.com/css2?family=Allura&family=Cormorant+Garamond:wght@400;500;600&display=swap" rel="stylesheet">
<style>
  :root {
    --backdrop: #eeece8;
    --card: #ffffff;
    --navy: #1f3350;
    --gold: #c9a068;
    --muted: #4a5563;
    --leaf: #4f7a52;
    --teal: #35596a;
    --dusk: #2a3f55;
    --ember: #8a5230;
    --night: #1f2d44;
  }
  * { margin: 0; padding: 0; box-sizing: border-box; }
  html, body {
    width: 1200px;
    height: 1200px;
    overflow: hidden;
    background: var(--backdrop);
  }
  .invitation {
    position: absolute;
    left: 237px;
    top: 40px;
    width: 726px;
    height: 1120px;
    background: var(--card);
    box-shadow: 0 6px 24px rgba(0, 0, 0, 0.12);
    overflow: hidden;
    text-align: center;
    font-family: "Cormorant Garamond", Georgia, serif;
  }
  .heading {
    position: absolute;
    top: 40px;
    left: 0;
    width: 100%;
    height: 130px;
  }
  .heading__kicker {
    position: absolute;
    top: 6px;
    left: 270px;
    font-size: 34px;
    letter-spacing: 3px;
    color: var(--gold);
    font-weight: 500;
  }
  .heading__script {
    position: absolute;
    top: 10px;
    left: 170px;
    font-family: "Allura", cursive;
    font-size: 128px;
    line-height: 1;
    color: var(--navy);
  }
  .venue {
    position: absolute;
    top: 172px;
    width: 100%;
    font-size: 27px;
    line-height: 31px;
    letter-spacing: 1.5px;
    color: var(--navy);
  }
  .day {
    position: absolute;
    top: 256px;
    width: 100%;
    font-size: 24px;
    font-weight: 600;
    letter-spacing: 1.5px;
    color: var(--navy);
  }
  .date {
    position: absolute;
    top: 296px;
    width: 100%;
    font-size: 64px;
    line-height: 1;
    letter-spacing: 4px;
    color: var(--gold);
  }
  .time {
    position: absolute;
    top: 372px;
    width: 100%;
    font-size: 26px;
    font-weight: 600;
    letter-spacing: 4px;
    color: var(--navy);
  }
  .weather {
    position: absolute;
    top: 410px;
    width: 100%;
    font-size: 25px;
    letter-spacing: 1.5px;
    color: var(--gold);
  }
  .note {
    position: absolute;
    top: 460px;
    width: 100%;
    font-size: 14px;
    letter-spacing: 0.4px;
    color: var(--muted);
  }
  .garden-scene {
    position: absolute;
    left: 0;
    bottom: 0;
    width: 100%;
    height: 590px;
    background:
      radial-gradient(ellipse 60% 40% at 60% 78%, rgba(214, 140, 70, 0.55), transparent 70%),
      linear-gradient(180deg, var(--leaf) 0%, var(--teal) 35%, var(--dusk) 60%, var(--ember) 82%, var(--night) 100%);
    clip-path: polygon(0 4%, 8% 2%, 18% 3%, 28% 1%, 40% 3%, 52% 1%, 62% 3%, 74% 2%, 86% 4%, 100% 3%, 100% 100%, 0 100%);
  }
</style>
</head>
<body>
  <main class="invitation">
    <header class="heading">
      <span class="heading__kicker">AFTERNOON</span>
      <h1 class="heading__script">Soirée</h1>
    </header>
    <p class="venue">MARLOW RESIDENCE<br>428 LINDEN AVE.</p>
    <p class="day">FRIDAY</p>
    <p class="date">07.17.2020</p>
    <p class="time">4:00 PM - 8:00 PM</p>
    <p class="weather">WEATHER PERMITTING</p>
    <p class="note">Please call 555-214-3087 if unsure. This is a 19+ event.</p>
    <div class="garden-scene" role="img" aria-label="Painted backyard garden party at dusk: guests gathered around a bonfire under tall trees strung with warm lights"></div>
  </main>
</body>
</html>
```